New Television Homescreen Template

We need a new default homescreen design for our televisions. This should reflect our company branding. My company is called Wardline Systems, WLS for short. Our website is www.wlsx.example. We develop televisions and infotainment solutions for the healthcare industry. I am somewhat open to different color palettes but our company colors are blue, black, and white. Our design is constrained by the 9 buttons, however the design of the buttons can be changed. Also, there is a video box on the right side of the screen as shown, this design can also be changed.

Target Market(s)

Hospital Patients

Requirements
Must have
• PSD template.

```html
<!DOCTYPE html>
<html lang="en">
<head>
<meta charset="utf-8">
<title>Wardline Systems – Television Homescreen</title>
<link rel="stylesheet" href="https://fonts.googleapis.com/css2?family=Nunito:wght@300;400&display=swap">
<style>
  :root {
    --backdrop: #e9e6e2;
    --screen-light: #2bb3e6;
    --screen-mid: #1a9fd6;
    --screen-deep: #137bb0;
    --side-panel: #1c5f80;
    --edge-line: #9fdcf3;
    --player-frame: #b9b9b9;
    --player-frame-edge: #9c9c9c;
    --player-screen: #fdf8f8;
    --play-icon: #d3d3d3;
    --control-icon: #ffffff;
    --button-face: #ffffff;
    --button-edge: #cfd9de;
    --button-text: #4ab7e2;
    --brand-text: #ffffff;
  }
  * { margin: 0; padding: 0; box-sizing: border-box; }
  html, body {
    width: 1200px; height: 758px; overflow: hidden;
    background: var(--backdrop);
    font-family: "Nunito", sans-serif;
  }
  .homescreen {
    position: absolute; left: 18px; top: 47px;
    width: 1164px; height: 655px; overflow: hidden;
    background: linear-gradient(160deg, var(--screen-light) 0%, var(--screen-mid) 55%, var(--screen-deep) 100%);
  }
  .homescreen-shapes { position: absolute; inset: 0; }
  .player {
    position: absolute; left: 20px; top: 65px;
    width: 822px; height: 532px;
    background: var(--player-frame);
    border: 1px solid var(--player-frame-edge);
    border-radius: 8px;
  }
  .player-screen {
    position: absolute; left: 13px; top: 10px;
    width: 800px; height: 456px;
    background: var(--player-screen);
    border-radius: 8px 8px 2px 2px;
  }
  .player-play { position: absolute; left: 339px; top: 125px; }
  .player-controls {
    position: absolute; left: 350px; top: 479px;
    display: flex; align-items: center; gap: 28px;
  }
  .brand {
    position: absolute; right: 14px; top: 26px;
    color: var(--brand-text);
    font-size: 27px; font-weight: 300; line-height: 1; letter-spacing: -0.2px;
    display: flex; align-items: center; gap: 8px;
  }
  .brand-mark {
    width: 14px; height: 14px; border: 2px solid var(--brand-text);
  }
  .channel-list {
    position: absolute; left: 955px; top: 107px;
    list-style: none;
  }
  .channel-button {
    display: flex; align-items: center; justify-content: flex-end;
    width: 212px; height: 50px; margin-bottom: 10.2px;
    padding-right: 26px;
    background: var(--button-face);
    border: 2px solid var(--button-edge); border-right: none;
    border-radius: 7px 0 0 7px;
    color: var(--button-text);
    font-size: 32px; font-weight: 300;
  }
</style>
</head>
<body>
  <main class="homescreen">
    <svg class="homescreen-shapes" width="1164" height="655" viewBox="0 0 1164 655" aria-hidden="true">
      <path d="M600 62 Q720 0 800 60" fill="none" stroke="#6fd0f2" stroke-width="10" opacity="0.45"/>
      <path d="M852 0 Q920 330 850 655 L1164 655 L1164 0 Z" fill="var(--side-panel)"/>
      <path d="M852 0 Q920 330 850 655" fill="none" stroke="var(--edge-line)" stroke-width="3"/>
    </svg>

    <section class="player" aria-label="Video player">
      <div class="player-screen">
        <svg class="player-play" width="162" height="186" viewBox="0 0 162 186" aria-label="Play">
          <polygon points="0,0 161,93 0,186" fill="var(--play-icon)"/>
        </svg>
      </div>
      <div class="player-controls">
        <svg width="38" height="38" viewBox="0 0 38 38" aria-label="Pause">
          <rect x="0" y="0" width="12" height="38" fill="var(--control-icon)"/>
          <rect x="25" y="0" width="12" height="38" fill="var(--control-icon)"/>
        </svg>
        <svg width="54" height="38" viewBox="0 0 54 38" aria-label="Volume">
          <polygon points="0,12 9,12 24,0 24,38 9,26 0,26" fill="var(--control-icon)"/>
          <path d="M38 4 Q48 19 38 34" fill="none" stroke="var(--control-icon)" stroke-width="3"/>
        </svg>
      </div>
    </section>

    <header class="brand"><span class="brand-mark"></span>Wardline Systems</header>

    <ul class="channel-list">
      <li class="channel-button">Cable TV</li>
      <li class="channel-button">Cable TV</li>
      <li class="channel-button">Cable TV</li>
      <li class="channel-button">Cable TV</li>
      <li class="channel-button">Cable TV</li>
      <li class="channel-button">Cable TV</li>
      <li class="channel-button">Cable TV</li>
      <li class="channel-button">Cable TV</li>
      <li class="channel-button">Cable TV</li>
    </ul>
  </main>
</body>
</html>
```